Book Cover Design - Uncovering Weight Loss Secrets

I need a book cover design for a book called 'Sorting Every Plate'. It is a book that goes through all of the secrets to weight loss, without any crazy shakes or workouts or pills or potions. The book is really focused on helping people understand that Weight loss is simple and has more to do with our mindset as well as the food we were eating. It is about taking personal responsibility not looking for the next fancy revolutionary product that is going to help them magically melt the fat away. The book is pragmatic in nature and breaks down in simple terms how we can lose weight and keep it off for the rest of our lives. It shows the user that it is simple to lose weight, but it takes effort. They should stop looking for a quick fix when it comes to weight loss but instead eat healthy for the rest of their lives.
The book is intended to be hard-hitting no holds barred approach. The book has the same title as my business name. I will attach the current logo that we use in the business. This doesn't need to be on the front of the book maybe at the back down the bottom somewhere.
I am looking to have both an e-book cover and a standard printed book cover.
I don't have any colours in mind, my logo can be adapted to be different colours or just white.
The message that I am wanting people to feel when they see my book, is that all these Weightloss fads are a joke, that I know the secrets that will get them to their weight loss goal even if they fail at everything else before.
On the cover it should say the following.
SORTING EVERY PLATE
Uncovering the Weight Loss Secrets
The big companies have been trying to keep hidden for years!
CALLUM FENWICK
Target Market(s)
People who have failed many times trying to lose weight & need help
Industry/Entity Type
Weight Loss
Look and feel

```html
<!DOCTYPE html>
<html lang="en">
<head>
<meta charset="utf-8">
<title>Sorting Every Plate – Book Cover</title>
<link href="https://fonts.googleapis.com/css2?family=Poppins:wght@400;500;700;800&display=swap" rel="stylesheet">
<style>
  :root {
    --page-bg: #ffffff;
    --navy: #0c2540;
    --navy-light: #1a3d66;
    --red: #d33a3f;
    --panel-light: #ececec;
    --panel-mid: #dcdcdc;
    --ink: #1d1d1d;
    --scale-dark: #4a4d50;
    --scale-mid: #6b6e71;
    --white: #ffffff;
  }
  * { margin: 0; padding: 0; box-sizing: border-box; }
  html, body {
    width: 800px;
    height: 1200px;
    overflow: hidden;
    background: var(--page-bg);
  }
  .canvas {
    position: relative;
    width: 800px;
    height: 1200px;
  }
  .book-cover {
    position: absolute;
    left: 40px;
    top: 60px;
    width: 720px;
    height: 1080px;
    background: var(--navy);
    box-shadow: 4px 6px 14px rgba(0,0,0,0.35);
    overflow: hidden;
  }
  .cover-panel {
    position: absolute;
    left: 18px;
    top: 18px;
    width: 684px;
    height: 962px;
    background:
      repeating-linear-gradient(90deg, rgba(0,0,0,0.025) 0 1px, transparent 1px 3px),
      repeating-linear-gradient(0deg, rgba(255,255,255,0.3) 0 1px, transparent 1px 4px),
      linear-gradient(180deg, var(--panel-light), var(--panel-mid));
  }
  .title-top {
    position: absolute;
    top: 20px;
    left: 0;
    width: 100%;
    text-align: center;
    font-family: "Poppins", sans-serif;
    font-weight: 700;
    font-size: 108px;
    line-height: 1;
    color: var(--red);
    letter-spacing: 2px;
  }
  .title-middle {
    position: absolute;
    top: 134px;
    left: 57px;
    width: 570px;
    display: flex;
    align-items: center;
    gap: 18px;
    font-family: "Poppins", sans-serif;
    font-weight: 700;
    font-size: 66px;
    line-height: 1;
    color: var(--red);
  }
  .title-middle .rule {
    flex: 1;
    height: 2px;
    background: var(--red);
  }
  .title-main {
    position: absolute;
    top: 178px;
    left: 0;
    width: 100%;
    text-align: center;
    font-family: "Poppins", sans-serif;
    font-weight: 800;
    font-size: 196px;
    line-height: 1;
    letter-spacing: -6px;
    background: linear-gradient(180deg, var(--navy), var(--navy-light) 60%, var(--navy));
    -webkit-background-clip: text;
    background-clip: text;
    color: transparent;
  }
  .cover-illustration {
    position: absolute;
    top: 356px;
    left: 57px;
    width: 570px;
    height: 430px;
    background: radial-gradient(ellipse 45% 50% at 50% 50%, var(--scale-dark), var(--scale-mid) 60%, rgba(220,220,220,0) 100%);
  }
  .subtitle-heading {
    position: absolute;
    top: 806px;
    left: 0;
    width: 100%;
    text-align: center;
    font-family: "Poppins", sans-serif;
    font-weight: 500;
    font-size: 31px;
    line-height: 1;
    color: var(--red);
  }
  .subtitle-body {
    position: absolute;
    top: 856px;
    left: 0;
    width: 100%;
    text-align: center;
    font-family: "Poppins", sans-serif;
    font-weight: 400;
    font-size: 24px;
    line-height: 32px;
    color: var(--ink);
  }
  .author-band {
    position: absolute;
    left: 0;
    bottom: 0;
    width: 100%;
    height: 100px;
    display: flex;
    align-items: center;
    justify-content: center;
    background: radial-gradient(ellipse at 50% 100%, var(--navy-light), var(--navy) 70%);
  }
  .author-name {
    font-family: "Poppins", sans-serif;
    font-weight: 700;
    font-size: 40px;
    letter-spacing: 9px;
    color: var(--white);
  }
</style>
</head>
<body>
<div class="canvas">
  <div class="book-cover">
    <div class="cover-panel">
      <h1 class="title-top">SORTING</h1>
      <div class="title-middle"><span class="rule"></span><span>EVERY</span><span class="rule"></span></div>
      <div class="title-main">PLATE</div>

      <div class="cover-illustration" role="img" aria-label="Illustration of a bathroom scale with a round dial, cinched at the waist by a yellow tape measure"></div>

      <h2 class="subtitle-heading">UNCOVERING THE WEIGHT LOSS SECRETS</h2>
      <p class="subtitle-body">The big companies have been trying<br>to keep hidden for years!</p>
    </div>
    <div class="author-band">
      <span class="author-name">CALLUM FENWICK</span>
    </div>
  </div>
</div>
</body>
</html>
```